Lanternfield Golf

I want main multi colored logo, with designer choosing a background of their choice for overall page, and then second upload (logo’s font) underneath, with address logo (but with following added right below phone number along with zip Code):

418 Calloway St
Suite 307C
Jersey City, NJ, 07348

a below a bit further down - to start.

Then we’ll take next steps.

```html
<!DOCTYPE html>
<html lang="en">
<head>
<meta charset="utf-8">
<title>Lanternfield Golf — Contact</title>
<link rel="stylesheet" href="https://fonts.googleapis.com/css2?family=Montserrat:wght@400;500;700&display=swap">
<style>
  :root {
    --gold: #e4ae18;
    --navy: #2d3553;
    --lavender: #b3bbe0;
    --ice: #d6dfff;
    --white: #ffffff;
    --stage: #cbced8;
    --frame-line: rgba(214, 223, 255, 0.35);
  }
  * { box-sizing: border-box; margin: 0; padding: 0; }
  html, body {
    width: 901px;
    height: 1200px;
    overflow: hidden;
    background: var(--stage);
    font-family: "Montserrat", sans-serif;
  }
  .contact-card {
    position: absolute;
    left: 0;
    top: 318px;
    width: 901px;
    height: 564px;
    background: var(--navy);
    overflow: hidden;
  }
  .backdrop-photo {
    position: absolute;
    inset: 0;
    background:
      radial-gradient(ellipse 120px 260px at 320px 250px, rgba(179, 187, 224, 0.07), transparent 70%),
      linear-gradient(115deg, transparent 45%, rgba(179, 187, 224, 0.05) 55%, transparent 70%);
  }
  .frame {
    position: absolute;
    left: 141px;
    top: 140px;
    width: 619px;
    height: 326px;
    border: 1px solid var(--frame-line);
    border-top: none;
  }
  .frame-top {
    position: absolute;
    top: 140px;
    height: 1px;
    background: var(--frame-line);
  }
  .frame-top--left { left: 141px; width: 225px; }
  .frame-top--right { left: 535px; width: 225px; }
  .brand-mark {
    position: absolute;
    left: 405px;
    top: 95px;
    width: 90px;
    height: 90px;
    border-radius: 50%;
    background: var(--gold);
  }
  .brand-name {
    position: absolute;
    left: 0;
    width: 901px;
    top: 222px;
    text-align: center;
    color: var(--white);
    font-weight: 700;
    font-size: 19px;
    line-height: 24px;
    letter-spacing: 0.2px;
  }
  .contact-details {
    position: absolute;
    left: 0;
    width: 901px;
    top: 300px;
    text-align: center;
    color: var(--ice);
    font-size: 10.5px;
    font-weight: 400;
  }
  .contact-details p { line-height: 14px; }
  .contact-details .name { margin-bottom: 6px; }
  .contact-details .company { margin-bottom: 6px; }
  .contact-details .email { margin-bottom: 8px; }
  .contact-details .phone { margin-bottom: 6px; }
  .inquiry-button {
    position: absolute;
    left: 382px;
    top: 447px;
    width: 138px;
    height: 38px;
    background: var(--gold);
    color: var(--white);
    font-size: 9px;
    font-weight: 700;
    letter-spacing: 0.2px;
    display: flex;
    align-items: center;
    justify-content: center;
    gap: 6px;
  }
</style>
</head>
<body>
  <section class="contact-card">
    <div class="backdrop-photo" role="img" aria-label="Faded navy-toned photo of a golfer mid-swing"></div>
    <div class="frame"></div>
    <div class="frame-top frame-top--left"></div>
    <div class="frame-top frame-top--right"></div>
    <div class="brand-mark"></div>
    <h1 class="brand-name">LANTERNFIELD<br>GOLF</h1>
    <div class="contact-details">
      <p class="name">M. Warren Hale</p>
      <p class="company">LANTERNFIELD GOLF</p>
      <p class="email">warren.hale@lanternfield.golf</p>
      <p class="phone">971 - 555 - 0142</p>
      <p class="address">418 Calloway St Suite 307C</p>
      <p class="address">Jersey City, NJ, 07348</p>
    </div>
    <div class="inquiry-button">
      <svg width="9" height="7" viewBox="0 0 9 7" aria-hidden="true">
        <rect x="0" y="0" width="9" height="7" fill="#ffffff"/>
        <path d="M0 0 L4.5 3.8 L9 0" fill="none" stroke="#e4ae18" stroke-width="1"/>
      </svg>
      <span>SEND EMAIL INQUIRY</span>
    </div>
  </section>
</body>
</html>
```